Boarding Pass for Tour Company

We need an A6 sized boarding pass desinged for our tour company.

Colours to follow company logo. Image background with white text on top.

Require a strip at the bottom with text on top. This will be a group indicator colour. Can use purple for design.

Font styles to use
Sans Serif

Colors
0054AA
0677BA
7BADD7
CADEEF
E8F1F8

```html
<!DOCTYPE html>
<html lang="en">
<head>
<meta charset="utf-8">
<title>Skyward Drift Boarding Pass</title>
<link rel="stylesheet" href="https://fonts.googleapis.com/css2?family=Anton&family=Exo+2:wght@600&display=swap">
<style>
  :root {
    --brand-deep: #0054AA;
    --brand-mid: #0677BA;
    --brand-sky: #3FA0DE;
    --brand-soft: #7BADD7;
    --brand-pale: #CADEEF;
    --brand-mist: #E8F1F8;
    --ink: #0b0b0b;
    --paper: #ffffff;
    --backdrop: #d9d9d9;
  }
  * { box-sizing: border-box; margin: 0; padding: 0; }
  html, body { width: 1200px; height: 800px; overflow: hidden; }
  body {
    background: var(--backdrop);
    display: flex;
    align-items: center;
    justify-content: center;
  }
  .pass {
    width: 517px;
    height: 720px;
    display: flex;
    flex-direction: column;
    background: var(--paper);
    box-shadow: 0 6px 18px rgba(0,0,0,.15);
  }
  .pass__header {
    height: 125px;
    display: flex;
    align-items: center;
    justify-content: center;
    gap: 12px;
    background: var(--paper);
  }
  .brand__dot {
    width: 22px; height: 22px;
    border-radius: 50%;
    background: var(--brand-sky);
  }
  .brand__name {
    font-family: "Exo 2", sans-serif;
    font-weight: 600;
    font-size: 38px;
    color: var(--brand-sky);
    letter-spacing: .5px;
  }
  .pass__scene {
    position: relative;
    height: 415px;
    background: linear-gradient(180deg,
      #3f86c9 0%, #6fa8d8 35%, #c8dcea 58%, #efe2c2 66%,
      #5f7038 74%, #6f8a2c 86%, #4f6a20 100%);
  }
  .pass__title {
    position: absolute;
    top: 72px;
    right: 28px;
    font-family: "Anton", sans-serif;
    font-size: 76px;
    line-height: 1.0;
    text-align: center;
    color: var(--paper);
    text-transform: uppercase;
    text-shadow:
      3px 0 0 var(--brand-sky), -3px 0 0 var(--brand-sky),
      0 3px 0 var(--brand-sky), 0 -3px 0 var(--brand-sky),
      2px 2px 0 var(--brand-sky), -2px -2px 0 var(--brand-sky),
      2px -2px 0 var(--brand-sky), -2px 2px 0 var(--brand-sky);
  }
  .pass__tag {
    height: 67px;
    background: var(--ink);
    display: flex;
    align-items: center;
    justify-content: center;
    font-family: "Exo 2", sans-serif;
    font-weight: 600;
    font-size: 22px;
    letter-spacing: 1px;
    color: var(--paper);
  }
  .pass__group {
    position: relative;
    height: 113px;
    background: var(--brand-sky);
    display: flex;
    align-items: center;
    justify-content: center;
    font-family: "Anton", sans-serif;
    font-size: 48px;
    color: var(--paper);
    text-transform: uppercase;
  }
  .pass__perforation {
    position: absolute;
    top: -3px; left: 0;
    width: 100%; height: 6px;
  }
</style>
</head>
<body>
  <main class="pass">
    <header class="pass__header">
      <span class="brand__dot"></span>
      <span class="brand__name">Skyward Drift</span>
    </header>
    <section class="pass__scene" role="img" aria-label="Photo of a brown and green hot air balloon over vineyards and gum trees under a blue morning sky">
      <h1 class="pass__title">Boarding<br>Pass</h1>
    </section>
    <div class="pass__tag">#skywarddrift</div>
    <div class="pass__group">
      <svg class="pass__perforation" viewBox="0 0 517 6" preserveAspectRatio="none" aria-hidden="true">
        <line x1="0" y1="3" x2="517" y2="3" stroke="#0b0b0b" stroke-width="4" stroke-dasharray="8 4"/>
      </svg>
      Pilot: Marcus
    </div>
  </main>
</body>
</html>
```